Leaf Haven Business Card Design

My E-Commerce store is called Leaf Haven

Website address is - http://www.leafhaven-demo.com.au

I would like a colourful, friendly business with the description in the 'must haves' box incorporated into it
Updates

Please add the following to the business cards; Natural & Organic Products Online Organic Pantry Items Superfoods & Supplements Natural Skincare Eco Friendly Household Products

Industry/Entity Type

Business

Contact Information for Business Card

www.leafhaven-demo.com.au
mira@leafhaven-demo.com.au

Colors
acd037
9bcb3c
cadf82
eaf2ce

Requirements
Must have
• Natural & Organic Eco Products Online.
• Leaf Haven specialises in organic pantry items, superfoods and supplements, organic skincare for you and your family & eco friendly household products.

```html
<!DOCTYPE html>
<html lang="en">
<head>
<meta charset="UTF-8">
<title>Leaf Haven Business Card</title>
<link href="https://fonts.googleapis.com/css2?family=Lato:wght@400;700&display=swap" rel="stylesheet">
<style>
  :root {
    --canvas-bg: #e9e7e3;
    --card-dark: #2a2a2a;
    --card-light: #ffffff;
    --lime: #acd037;
    --lime-deep: #9bcb3c;
    --lime-soft: #cadf82;
    --lime-pale: #eaf2ce;
    --lime-text: #7fa823;
    --text-grey: #555555;
    --divider: #e4e4e4;
  }
  html, body {
    margin: 0;
    padding: 0;
    width: 1200px;
    height: 1000px;
    overflow: hidden;
    background: var(--canvas-bg);
    font-family: "Lato", sans-serif;
  }
  .canvas {
    position: relative;
    width: 1200px;
    height: 1000px;
  }
  .card {
    position: absolute;
    left: 275px;
    width: 650px;
    height: 370px;
    border-radius: 22px;
    box-shadow: 0 6px 18px rgba(0,0,0,0.18);
    overflow: hidden;
  }
  .card-front {
    top: 113px;
    background: var(--card-dark);
    display: flex;
    flex-direction: column;
    align-items: center;
    justify-content: center;
    gap: 18px;
  }
  .card-back {
    top: 517px;
    background: var(--card-light);
  }
  .brand {
    display: flex;
    align-items: center;
    gap: 16px;
    color: var(--lime);
    font-weight: 400;
  }
  .brand-dot {
    border-radius: 50%;
    background: var(--lime-deep);
    flex: none;
  }
  .brand-front .brand-name { font-size: 56px; line-height: 1; }
  .brand-front .brand-dot { width: 26px; height: 26px; }
  .front-tagline {
    margin: 0;
    font-size: 16px;
    letter-spacing: 1.5px;
    text-transform: uppercase;
    color: var(--lime-soft);
  }
  .brand-back {
    position: absolute;
    right: 375px;
    top: 170px;
    transform: translateY(-50%);
    gap: 10px;
    color: var(--lime-text);
  }
  .brand-back .brand-name { font-size: 25px; }
  .brand-back .brand-dot { width: 14px; height: 14px; background: var(--lime); }
  .divider {
    position: absolute;
    left: 306px;
    top: 114px;
    width: 1px;
    height: 112px;
    background: var(--divider);
  }
  .contact-block {
    position: absolute;
    left: 339px;
    top: 105px;
  }
  .person-name {
    margin: 0;
    font-size: 19px;
    font-weight: 700;
    color: var(--lime-text);
    line-height: 24px;
  }
  .person-role {
    margin: 0 0 22px;
    font-size: 15px;
    color: var(--text-grey);
    line-height: 18px;
  }
  .contact-list {
    list-style: none;
    margin: 0;
    padding: 0;
  }
  .contact-list li {
    display: flex;
    align-items: center;
    gap: 5px;
    font-size: 14.5px;
    color: var(--text-grey);
    line-height: 25px;
  }
  .contact-list svg {
    width: 12px;
    height: 12px;
    flex: none;
  }
  .product-band {
    position: absolute;
    left: 0;
    right: 0;
    bottom: 0;
    height: 54px;
    background: var(--lime-pale);
    border-top: 3px solid var(--lime);
    display: flex;
    align-items: center;
    justify-content: center;
    gap: 10px;
    font-size: 12.5px;
    color: var(--text-grey);
  }
  .product-band .sep {
    width: 5px;
    height: 5px;
    border-radius: 50%;
    background: var(--lime-deep);
  }
</style>
</head>
<body>
<main class="canvas">
  <section class="card card-front" aria-label="Business card front">
    <div class="brand brand-front">
      <span class="brand-dot"></span>
      <span class="brand-name">Leaf Haven</span>
    </div>
    <p class="front-tagline">Natural &amp; Organic Products Online</p>
  </section>

  <section class="card card-back" aria-label="Business card back">
    <div class="brand brand-back">
      <span class="brand-dot"></span>
      <span class="brand-name">Leaf Haven</span>
    </div>
    <div class="divider"></div>
    <div class="contact-block">
      <p class="person-name">Daniel Roe</p>
      <p class="person-role">Founder &amp; CEO</p>
      <ul class="contact-list">
        <li>
          <svg viewBox="0 0 24 24" aria-hidden="true"><path fill="#9bcb3c" d="M6.6 10.8a15 15 0 0 0 6.6 6.6l2.2-2.2c.3-.3.7-.4 1-.2 1.1.4 2.3.6 3.6.6.6 0 1 .4 1 1V20c0 .6-.4 1-1 1A17 17 0 0 1 3 4c0-.6.4-1 1-1h3.5c.6 0 1 .4 1 1 0 1.3.2 2.5.6 3.6.1.3 0 .7-.2 1z"/></svg>
          014 555 0192
        </li>
        <li>
          <svg viewBox="0 0 24 24" aria-hidden="true"><path fill="#9bcb3c" d="M2 5h20v14H2z"/><path fill="none" stroke="#fff" stroke-width="2" d="M2 6l10 7 10-7"/></svg>
          mira@leafhaven-demo.com.au
        </li>
        <li>
          <svg viewBox="0 0 24 24" aria-hidden="true"><g fill="none" stroke="#9bcb3c" stroke-width="2"><circle cx="12" cy="12" r="10"/><ellipse cx="12" cy="12" rx="4" ry="10"/><path d="M2 12h20M4 7h16M4 17h16"/></g></svg>
          www.leafhaven-demo.com.au
        </li>
      </ul>
    </div>
    <div class="product-band">
      <span>Organic Pantry Items</span><span class="sep"></span>
      <span>Superfoods &amp; Supplements</span><span class="sep"></span>
      <span>Natural Skincare</span><span class="sep"></span>
      <span>Eco Friendly Household Products</span>
    </div>
  </section>
</main>
</body>
</html>
```